Zielgruppe
We are an event technology rental company specializing in corporate events and conferences. Our services include audio and video rental, LED video walls, and full technical support for business events of all sizes
Aufgabenstellung
Objective:
To design and develop a modern, visually appealing website that effectively communicates our brand values: experience, trustworthiness, and professionalism. The site should support our sales and marketing efforts by showcasing our services, building credibility, and making it easy for potential clients to get in touch.
Creative Direction:
• The website should feature eye-catching visuals
• It should have a clean, professional design with a user-friendly interface and intuitive navigation.
• The look and feel must reflect technical competence, reliability, and high-end service.
Content & Structure Guidelines:
A basic guide with suggested sections is provided in the attachment.
⚠️ Please note:
• The guide is not a layout or color reference.
• It serves only to suggest the types of content sections we want.
• The order of sections is flexible — we welcome your creative interpretation.
Header Feature:
The website header should be designed to support a 10–12 second video in the future. For now, please use a stock photo (not one of our own images) as a placeholder.
Visual & UX Expectations:
• Strong visual hierarchy and clarity.
• Mobile-optimized, responsive design.
• Fast-loading and modern layout.
• Clear calls to action such as “Contact” or “Request a Quote”
• A smooth, professional user experience with a focus on technical services.

```html
<!DOCTYPE html>
<html lang="en">
<head>
<meta charset="utf-8">
<title>Bühnenwerk Linz – Event Technology</title>
<link href="https://fonts.googleapis.com/css2?family=Inter:wght@300;400;500;600;700&display=swap" rel="stylesheet">
<style>
:root{
  --teal:#009b86;
  --cyan:#00ace2;
  --ink:#141414;
  --muted:#555;
  --line:#dcdcdc;
  --night:#0a1240;
  --maroon:#3b0f12;
  --white:#fff;
}
*{box-sizing:border-box;margin:0;padding:0}
html,body{width:1200px;height:4118px;overflow:hidden}
body{font-family:"Inter",sans-serif;color:var(--ink);background:var(--white);position:relative}
.abs{position:absolute}
.btn{position:absolute;display:flex;align-items:center;justify-content:center;border-radius:30px;font-size:12px;font-weight:600;letter-spacing:.3px;text-transform:uppercase}
.btn-teal{background:var(--teal);color:#fff}
.btn-white{background:#fff;color:var(--ink)}
.photo{position:absolute}
/* nav */
.nav{left:60px;top:0;width:1080px;height:75px;border-radius:0 0 40px 40px;background:rgba(200,200,210,.55);}
.brand{left:95px;top:20px;display:flex;align-items:center;gap:12px}
.brand-dot{width:30px;height:30px;border-radius:50%;border:3px solid #222}
.brand-name{font-size:12px;font-weight:600;line-height:1.1;color:#222}
.brand-name span{display:block;font-weight:400}
.menu{left:390px;top:29px;display:flex;gap:38px;font-size:14px;color:#333}
.menu .on{font-weight:700;color:#111;border-bottom:2px solid #111;padding-bottom:4px}
/* hero */
.hero{left:0;top:0;width:1200px;height:740px;background:radial-gradient(ellipse at 70% 35%,#5a7fe0 0%,#233a95 30%,#0e1a55 60%,#060b2a 100%)}
.hero h1{left:62px;top:218px;font-size:47px;font-weight:400;color:#fff;line-height:63px}
.hero p{left:62px;top:355px;width:620px;font-size:11.5px;color:#e8ecff;line-height:16px}
.play{left:976px;top:311px;width:70px;height:70px;border-radius:50%;background:#fff;display:flex;align-items:center;justify-content:center}
/* about */
.about-h{left:688px;top:852px;font-size:30px;font-weight:400}
.about-t{left:688px;top:902px;font-size:39px;font-weight:400;line-height:48px}
.para{font-size:12.5px;color:#555;line-height:19px}
.bul{display:flex;align-items:center;gap:10px;font-size:15px;color:#222;position:absolute}
.bul::before{content:"";width:13px;height:13px;border-radius:50%;background:var(--teal)}
.sc{font-variant:small-caps;font-size:15px}
/* services */
.services{left:0;top:1360px;width:1200px;height:456px;background:var(--cyan)}
.card{position:absolute;top:227px;width:258px;height:160px;background:#fff;border-radius:14px 14px 0 0;text-align:center;padding-top:12px;border-bottom:5px solid #111}
.card.grey{background:#dedede;border-bottom-color:#1b3ccf}
.card h4{font-size:15px;font-weight:400;margin:16px 0 14px}
.card p{font-size:12.5px;color:#444;line-height:19px}
.ico{width:40px;height:36px;margin:0 auto;border:2px solid #444;border-radius:4px}
/* how */
.tab{position:absolute;left:66px;width:245px;height:56px;border:1.5px solid var(--line);border-radius:12px;display:flex;align-items:center;gap:12px;padding-left:16px;font-size:14px;font-weight:500}
.tab i{width:38px;height:38px;border-radius:50%;background:#d8d8d8;display:block}
.tab.on{background:var(--teal);color:#fff;border-color:var(--teal)}
.tab.on i{background:#fff}
.center{position:absolute;left:0;width:1200px;text-align:center}
/* gallery */
.g{position:absolute;border-radius:8px}
.arrow{position:absolute;top:2975px;width:36px;height:36px;border-radius:50%;background:var(--maroon)}
/* contact */
.form{left:441px;top:3200px;width:550px;height:335px;border:2px solid #ddd;border-radius:22px}
.field{position:absolute;border:1.5px solid #ccc;border-radius:4px;font-size:13px;padding:6px 14px;color:#222;height:30px}
.ci{position:absolute;left:87px;font-size:12.5px;line-height:20px}
.ci b{font-weight:400;font-size:12px;display:block}
.soc{display:inline-block;width:14px;height:14px;border-radius:3px;background:#222;margin-right:5px;vertical-align:middle}
/* footer */
.footer{left:0;top:3718px;width:1200px;height:400px;background:radial-gradient(ellipse at 20% 10%,#2b50d8 0%,#0d1a6a 35%,#070d3a 70%)}
.fcol{position:absolute;color:#fff;font-size:14px;line-height:36px}
.fcol h5{font-size:14px;font-weight:500;line-height:22px;margin-bottom:4px}
</style>
</head>
<body>

<section class="abs hero" role="img" aria-label="Conference hall with stage, blue spotlights and audience seated in rows">
</section>
<svg class="abs" style="left:0;top:650px" width="1200" height="100" viewBox="0 0 1200 100" aria-hidden="true">
  <path d="M0 80 Q600 -30 1200 80 L1200 100 L0 100Z" fill="#cfcfcf"/>
  <path d="M0 95 Q600 0 1200 95 L1200 100 L0 100Z" fill="#fff"/>
</svg>
<div class="abs hero" style="background:none;height:0">
  <h1 class="abs">Your Event. Our Technology.<br>Flawless Execution</h1>
  <p class="abs">Lorem ipsum dolor sit amet, consectetur adipiscing elit, sed do eiusmod tempor incididunt ut labore et dolore magna aliqua. Ut enim ad minim veniam, quis nostrud exercitation ullamco laboris nisi ut aliquip ex ea commodo consequat. Duis aute irure dolor in reprehenderit in voluptate velit esse cillum dolore eu</p>
</div>
<a class="btn btn-white" style="left:62px;top:428px;width:142px;height:45px">Learn More</a>
<div class="abs play"><svg width="20" height="22" viewBox="0 0 20 22"><path d="M3 1 L19 11 L3 21Z" fill="#111"/></svg></div>

<header>
  <div class="abs nav"></div>
  <div class="abs brand"><span class="brand-dot"></span><span class="brand-name">Bühnenwerk Linz<span>Veranstaltungs GmbH</span></span></div>
  <nav class="abs menu"><span class="on">Home</span><span>About Us</span><span>Services</span><span>Gallery</span><span>How It Works</span></nav>
  <a class="btn btn-teal" style="left:964px;top:17px;width:142px;height:44px">Contact Us</a>
</header>

<section>
  <div class="photo" style="left:112px;top:818px;width:345px;height:414px;border-radius:14px;background:linear-gradient(160deg,#3a1f5c,#1a0f1c 50%,#6a3b10)" role="img" aria-label="Mixing console in front of a lit concert stage"></div>
  <div class="photo" style="left:422px;top:920px;width:233px;height:213px;border-radius:10px;background:#fff"></div>
  <div class="photo" style="left:430px;top:930px;width:217px;height:195px;border-radius:6px;background:linear-gradient(160deg,#3b2a88,#7d8b1a 55%,#1a1a2a)" role="img" aria-label="Lighting desk with yellow and purple stage beams"></div>
  <h3 class="abs about-h">About Us</h3>
  <h2 class="abs about-t">Driven by Experience.<br>Defined by Precision</h2>
  <p class="abs para" style="left:688px;top:1008px;width:400px">Lorem ipsum dolor sit amet, consectetur adipiscing elit, sed do eiusmod tempor incididunt ut labore et dolore magna aliqua. Ut enim ad minim veniam, quis nostrud exercitation ullamco laboris nisi ut aliquip ex ea commodo consequat. Duis aute irure</p>
  <div class="bul" style="left:682px;top:1106px">Professionalism</div>
  <div class="bul" style="left:682px;top:1142px">Technical Expertise</div>
  <div class="bul" style="left:682px;top:1178px">Trust &amp; Reliability</div>
  <a class="btn btn-teal" style="left:682px;top:1220px;width:140px;height:47px">Learn More</a>
  <div class="photo" style="left:857px;top:1217px;width:52px;height:52px;border-radius:50%;background:linear-gradient(#c9ccd2,#6d7380)" role="img" aria-label="Portrait of the managing director"></div>
  <div class="abs" style="left:916px;top:1227px;font-size:11px;color:#555;font-variant:small-caps;line-height:14px">Marlen<br>Haubner</div>
</section>

<section class="abs services">
  <h3 class="abs" style="left:58px;top:48px;font-size:31px;font-weight:400;color:#fff">Services</h3>
  <h2 class="abs" style="left:58px;top:102px;font-size:38px;font-weight:400;color:#fff;line-height:48px">Reliable AV &amp; LED Services<br>Tailored for Business Events</h2>
  <a class="btn btn-white" style="left:987px;top:102px;width:141px;height:44px">Learn More</a>
  <div class="card grey" style="left:58px"><div class="ico"></div><h4>Led Video</h4><p>Lorem ipsum dolor sit amet,<br>consectetur adipiscing elit, sed do</p></div>
  <div class="card" style="left:333px"><div class="ico"></div><h4>Technical Support</h4><p>Lorem ipsum dolor sit amet,<br>consectetur adipiscing elit, sed do</p></div>
  <div class="card" style="left:608px"><div class="ico"></div><h4>Event Planning</h4><p>Lorem ipsum dolor sit amet,<br>consectetur adipiscing elit, sed do</p></div>
  <div class="card" style="left:884px"><div class="ico" style="border-radius:50%"></div><h4>Remote Monitoring</h4><p>Lorem ipsum dolor sit amet,<br>consectetur adipiscing elit, sed do</p></div>
</section>

<section>
  <h3 class="center" style="top:1902px;font-size:30px;font-weight:500">How It Works</h3>
  <h2 class="center" style="top:1950px;font-size:38px;font-weight:400">Effortless Setup Flawless Results</h2>
  <div class="tab" style="top:2040px"><i></i>Consultation Planning</div>
  <div class="tab on" style="top:2117px"><i></i>Setup &amp; Execution</div>
  <div class="tab" style="top:2195px"><i></i>On-Site Support</div>
  <div class="tab" style="top:2272px"><i></i>Custom Proposal</div>
  <div class="photo" style="left:336px;top:2040px;width:441px;height:310px;border-radius:10px;background:linear-gradient(170deg,#b8a8e8,#6b3fc4 40%,#2a1560)" role="img" aria-label="Banquet hall with round tables and purple LED walls"></div>
  <h3 class="abs" style="left:805px;top:2034px;font-size:25px;font-weight:400">Consultation Planning</h3>
  <p class="abs para" style="left:805px;top:2085px;width:320px">Lorem ipsum dolor sit amet, consectetur adipiscing elit, sed do eiusmod tempor incididunt ut labore et dolore magna aliqua. Ut enim ad minim veniam, quis nostrud exercitation ullamco laboris nisi ut aliquip ex ea commodo consequat. Duis aute irure</p>
  <div class="bul sc" style="left:806px;top:2201px">Professionalism</div>
  <div class="bul sc" style="left:806px;top:2237px">Technical Expertise</div>
  <div class="bul sc" style="left:806px;top:2273px">Trust &amp; Reliability</div>
  <a class="btn btn-teal" style="left:809px;top:2312px;width:151px;height:46px;font-weight:500">Learn More</a>
</section>

<section>
  <h3 class="center" style="top:2447px;font-size:30px;font-weight:500">Gallery</h3>
  <h2 class="center" style="top:2498px;font-size:38px;font-weight:400">Real Events. Real Impact. Real Results</h2>
  <div class="g" style="left:187px;top:2570px;width:346px;height:380px;background:linear-gradient(160deg,#1b2440,#2e7fb0 45%,#141826)" role="img" aria-label="Audience facing a conference stage with screens"></div>
  <div class="g" style="left:549px;top:2570px;width:225px;height:187px;background:radial-gradient(#6cc4ff,#1c4fd0 45%,#050a30)" role="img" aria-label="Stage with blue LED screens"></div>
  <div class="g" style="left:789px;top:2570px;width:225px;height:187px;background:linear-gradient(#0a1a4a,#2a70c8 60%,#0a0f30)" role="img" aria-label="Speaker on a stage lit in blue"></div>
  <div class="g" style="left:549px;top:2770px;width:225px;height:185px;background:linear-gradient(#1a2a80,#c04a9a 60%,#301030)" role="img" aria-label="Concert crowd under light beams"></div>
  <div class="g" style="left:789px;top:2770px;width:225px;height:185px;background:radial-gradient(#4a5ae0,#0e1450 50%,#02030c)" role="img" aria-label="Dark hall with a lit projection wall"></div>
  <div class="arrow" style="left:560px"><svg width="36" height="36"><path d="M25 18H11M16 13l-5 5 5 5" stroke="#fff" stroke-width="2" fill="none"/></svg></div>
  <div class="arrow" style="left:605px"><svg width="36" height="36"><path d="M11 18h14M20 13l5 5-5 5" stroke="#fff" stroke-width="2" fill="none"/></svg></div>
</section>

<section>
  <h3 class="abs" style="left:87px;top:3197px;font-size:31px;font-weight:500">Contact Us</h3>
  <h2 class="abs" style="left:87px;top:3250px;font-size:38px;font-weight:400">Lets Gets In Touchs</h2>
  <div class="abs" style="left:87px;top:3328px;font-size:14px;font-weight:700">INFO</div>
  <div class="ci" style="top:3362px;left:113px"><b>Phone</b>(312) 555-0147</div>
  <div class="ci" style="top:3420px;left:118px"><b>Email</b>kontakt@buehnenwerk.example</div>
  <div class="ci" style="top:3477px;left:112px"><b>Adress</b>Hafenstraße 18, Linz 4020</div>
  <svg class="abs" style="left:86px;top:3364px" width="18" height="140" aria-hidden="true" fill="none" stroke="var(--teal)" stroke-width="1.5">
    <path d="M3 2c0 8 5 13 13 13l1-3-4-2-2 2c-3-1-4-3-5-5l2-2-2-4z"/>
    <rect x="1" y="57" width="16" height="11"/><path d="M1 57l8 6 8-6"/>
    <path d="M9 128c-5-6-6-8-6-11a6 6 0 0 1 12 0c0 3-1 5-6 11z"/><circle cx="9" cy="117" r="2"/>
  </svg>
  <div class="abs" style="left:112px;top:3536px;font-size:12px">Social Media &nbsp; <span class="soc"></span><span class="soc"></span><span class="soc"></span><span class="soc" style="border-radius:50%"></span></div>

  <div class="abs form"></div>
  <div class="field" style="left:491px;top:3241px;width:218px">Name</div>
  <div class="field" style="left:723px;top:3240px;width:218px">Phone</div>
  <div class="field" style="left:491px;top:3298px;width:218px">Email</div>
  <div class="field" style="left:723px;top:3298px;width:218px">Adress</div>
  <div class="field" style="left:490px;top:3353px;width:454px;height:86px;border-radius:8px">Message</div>
  <a class="btn btn-teal" style="left:490px;top:3462px;width:454px;height:34px;text-transform:none;font-size:13px">Submit</a>
</section>

<footer class="abs footer" role="img" aria-label="Dark stage backdrop with blue spotlights">
  <div class="abs" style="left:58px;top:65px;width:50px;height:50px;border-radius:50%;border:5px solid #fff"></div>
  <div class="abs" style="left:126px;top:55px;width:2px;height:70px;background:#fff"></div>
  <div class="abs" style="left:143px;top:80px;color:#fff;font-size:20px;font-weight:600;line-height:20px">Bühnenwerk Linz<br><span style="font-weight:400">Veranstaltungs GmbH</span></div>
  <div class="abs" style="left:60px;top:188px"><span class="soc" style="background:#fff;margin-right:10px"></span><span class="soc" style="background:#fff;margin-right:10px"></span><span class="soc" style="background:#fff;margin-right:10px"></span><span class="soc" style="background:#fff;border-radius:50%"></span></div>
  <div class="fcol" style="left:584px;top:92px"><h5>Quick Links</h5>Home<br>About Us<br>Services<br>Gallery<br>How It Works</div>
  <div class="fcol" style="left:768px;top:92px"><h5 style="font-size:19px;font-weight:400">Legal</h5>Privacy Policy<br>Terms Of Use<br>Cookie Policy</div>
  <svg class="abs" style="left:922px;top:92px" width="40" height="230" aria-hidden="true" fill="none" stroke="#fff" stroke-width="2">
    <path d="M5 4c0 16 10 26 26 26l3-7-8-4-4 4c-5-2-8-5-10-10l4-4-4-8z"/>
    <rect x="3" y="82" width="32" height="22"/><path d="M3 82l16 12 16-12"/>
    <path d="M19 188c-10-11-12-15-12-20a12 12 0 0 1 24 0c0 5-2 9-12 20z"/><circle cx="19" cy="168" r="4"/>
  </svg>
  <div class="fcol" style="left:977px;top:88px;font-size:13px;line-height:18px">Phone<br>(312) 555-0147</div>
  <div class="fcol" style="left:977px;top:162px;font-size:13px;line-height:18px">Email<br>kontakt@buehnenwerk.example</div>
  <div class="fcol" style="left:977px;top:252px;font-size:13px;line-height:18px">Adress<br>Hafenstraße 18,<br>Linz 4020</div>
  <div class="abs" style="left:0;top:322px;width:1200px;height:1px;background:rgba(255,255,255,.35)"></div>
  <div class="abs" style="left:0;top:340px;width:1200px;text-align:center;color:#fff;font-size:11px">Copyright © 2025. All Rights Reserved.</div>
</footer>

</body>
</html>
```